R&t Subterra

We specialize in CIPP pipe lining but do other underground utilities trenchless as well.

Target Market(s)

Trenchless sewer replacement

Contact Information for Business Card

Gavin Holtby 555-482-6130 Cedar hollow, mn

```html
<!DOCTYPE html>
<html lang="en">
<head>
<meta charset="utf-8">
<title>R&amp;T Subterra – Business Card</title>
<link rel="stylesheet" href="https://fonts.googleapis.com/css2?family=Montserrat:wght@400;500;700&display=swap">
<style>
  :root {
    --canvas: #d9d9d9;
    --card-white: #ffffff;
    --card-black: #1a1a1a;
    --emboss: #0e0e0e;
    --brand-blue: #3590cf;
    --band-blue: #0f6fc0;
    --band-grey: #b1b1b1;
    --ink: #1c1c1c;
  }
  * { margin: 0; padding: 0; box-sizing: border-box; }
  html, body { width: 1200px; height: 895px; overflow: hidden; }
  body {
    background: var(--canvas);
    font-family: "Montserrat", Arial, sans-serif;
    display: flex;
    flex-direction: column;
    align-items: center;
    justify-content: center;
    gap: 40px;
  }
  .card {
    position: relative;
    width: 620px;
    height: 354px;
    overflow: hidden;
    box-shadow: 0 6px 18px rgba(0,0,0,.25);
  }
  /* back side */
  .card--back {
    background: var(--card-black);
    display: flex;
    align-items: center;
    justify-content: center;
  }
  .card--back .brand-name {
    color: var(--emboss);
    font-size: 46px;
    font-weight: 700;
    display: flex;
    align-items: center;
    gap: 18px;
  }
  .card--back .brand-dot { background: var(--emboss); width: 54px; height: 54px; }
  /* front side */
  .card--front { background: var(--card-white); }
  .brand {
    position: absolute;
    left: 150px;
    top: 62px;
    display: flex;
    align-items: center;
    gap: 16px;
  }
  .brand-dot { width: 60px; height: 60px; border-radius: 50%; background: var(--brand-blue); }
  .card--front .brand-name {
    color: var(--brand-blue);
    font-size: 44px;
    font-weight: 700;
  }
  .person {
    position: absolute;
    left: 150px;
    top: 196px;
    width: 200px;
    text-align: right;
  }
  .person-name { color: var(--brand-blue); font-size: 24px; font-weight: 700; margin-bottom: 4px; }
  .person-role, .person-town { color: var(--ink); font-size: 15px; font-weight: 500; line-height: 1.35; }
  .divider {
    position: absolute;
    left: 372px;
    top: 176px;
    width: 2px;
    height: 92px;
    background: var(--brand-blue);
  }
  .contacts {
    position: absolute;
    left: 392px;
    top: 178px;
    list-style: none;
  }
  .contacts li {
    display: flex;
    align-items: center;
    gap: 12px;
    color: var(--ink);
    font-size: 15px;
    font-weight: 500;
    height: 30px;
  }
  .contacts svg { width: 18px; height: 18px; fill: var(--brand-blue); flex: none; }
  .bands { position: absolute; left: 0; bottom: 0; width: 620px; height: 40px; }
</style>
</head>
<body>
  <section class="card card--back" aria-label="Card back">
    <div class="brand-name"><span class="brand-dot"></span>R&amp;T Subterra</div>
  </section>

  <section class="card card--front" aria-label="Card front">
    <div class="brand">
      <span class="brand-dot"></span>
      <span class="brand-name">R&amp;T Subterra</span>
    </div>

    <div class="person">
      <p class="person-name">Gavin Holtby</p>
      <p class="person-role">Managing Director</p>
      <p class="person-town">Cedar hollow, mn</p>
    </div>

    <div class="divider"></div>

    <ul class="contacts">
      <li>
        <svg viewBox="0 0 24 24"><path d="M6.6 10.8a15.1 15.1 0 0 0 6.6 6.6l2.2-2.2a1 1 0 0 1 1-.25 11.4 11.4 0 0 0 3.6.57 1 1 0 0 1 1 1V20a1 1 0 0 1-1 1A17 17 0 0 1 3 4a1 1 0 0 1 1-1h3.5a1 1 0 0 1 1 1c0 1.25.2 2.45.57 3.57a1 1 0 0 1-.25 1z"/></svg>
        555-482-6130
      </li>
      <li>
        <svg viewBox="0 0 24 24"><path d="M2 5h20v2l-10 6L2 7zM2 9l10 6 10-6v10H2z"/></svg>
        info@rtsubterra.com
      </li>
      <li>
        <svg viewBox="0 0 24 24"><circle cx="12" cy="12" r="10"/><path d="M2 12h20M12 2c3 3 3 17 0 20M12 2c-3 3-3 17 0 20" stroke="#fff" stroke-width="1.5" fill="none"/></svg>
        www.rtsubterra.com
      </li>
    </ul>

    <svg class="bands" viewBox="0 0 620 40" preserveAspectRatio="none" aria-hidden="true">
      <polygon points="0,28 440,28 428,40 0,40" fill="var(--band-blue)"/>
      <polygon points="452,14 620,14 620,40 438,40" fill="var(--band-grey)"/>
    </svg>
  </section>
</body>
</html>
```